Redesign our business card for more impact

We want to completely replace the back design of our card, and refresh or even change the front entirely. We are happy with our black K4 logo and do not want to change it.
Our company address changed too. It is now 2307 Larkmoor, Alder, CA 92741
Updates

It was reported by Art Harbor email today that the uploaded files didnt upload. I am trying again.

Target Market(s)

Architects and Building Owners (People making multi-million dollar decisions)

Industry/Entity Type

Consulting Engineering

Contact Information for Business Card

Contact info on the front. "wallpaper" design on back with tag line on the back "Designing Tomorrow Now"

Font styles to use
Sans Serif

Requirements
Must have
• A vivid, modern, impactful ...but tasteful back of card design. It should communicate our premier status, but grab attention as innovative. DESIGN SHOULD BE ELEGANT AND NOT TOO BUSY.
Nice to have
• Repeating pattern, multi-color, something creative...
Should not have
• Anything that looks too playful or that we are not serious professionals. It should also not be too boring or conservative.

```html
<!DOCTYPE html>
<html lang="en">
<head>
<meta charset="utf-8">
<title>K4 Engineering Business Card</title>
<link rel="stylesheet" href="https://fonts.googleapis.com/css2?family=Inter:wght@400;700;800&display=swap">
<style>
  :root {
    --page-bg: #e6e6e6;
    --card-white: #ffffff;
    --ink-dark: #2b2b2b;
    --accent-red: #cc1f2a;
    --text-grey: #555555;
    --rule-grey: #8a8a8a;
    --pattern-dark: #1c1c1c;
    --pattern-mid: #4a4a4a;
    --pattern-light: #6a6a6a;
    --reverse-white: #ffffff;
  }
  * { margin: 0; padding: 0; box-sizing: border-box; }
  html, body {
    width: 1192px;
    height: 1200px;
    overflow: hidden;
    background: var(--page-bg);
    font-family: "Inter", sans-serif;
  }
  .card {
    position: absolute;
    left: 248px;
    width: 697px;
    height: 397px;
    border-radius: 30px;
    overflow: hidden;
  }
  .card-front { top: 160px; background: var(--card-white); }
  .card-back { top: 641px; }

  .wordmark {
    position: absolute;
    left: 0;
    width: 100%;
    text-align: center;
    font-weight: 800;
    line-height: 1;
    letter-spacing: -2px;
    white-space: nowrap;
  }
  .card-front .wordmark {
    top: 44px;
    font-size: 124px;
    color: var(--ink-dark);
  }

  .identity {
    position: absolute;
    right: 371px;
    top: 244px;
    text-align: right;
    color: var(--accent-red);
    white-space: nowrap;
  }
  .identity .name {
    font-weight: 700;
    font-size: 24px;
    line-height: 30px;
  }
  .identity .credentials,
  .identity .role {
    font-weight: 400;
    font-size: 18.5px;
    line-height: 23px;
  }

  .divider {
    position: absolute;
    left: 350px;
    top: 236px;
    width: 1px;
    height: 100px;
    background: var(--rule-grey);
  }

  .contact {
    position: absolute;
    left: 374px;
    top: 230px;
    list-style: none;
    color: var(--text-grey);
    font-size: 18.5px;
    line-height: 27.5px;
    white-space: nowrap;
  }

  .pattern-field {
    position: absolute;
    inset: 0;
    background:
      linear-gradient(135deg, var(--pattern-mid) 0%, var(--pattern-dark) 35%, var(--pattern-light) 55%, var(--pattern-dark) 80%, var(--pattern-mid) 100%);
  }
  .card-back .wordmark {
    top: 86px;
    font-size: 185px;
    color: var(--reverse-white);
  }
  .tagline {
    position: absolute;
    left: 0;
    top: 338px;
    width: 100%;
    text-align: center;
    color: var(--reverse-white);
    font-size: 18px;
    line-height: 1;
    letter-spacing: 3.6px;
    font-weight: 400;
    white-space: nowrap;
  }
</style>
</head>
<body>
  <section class="card card-front" aria-label="Business card front">
    <div class="wordmark">K4</div>
    <div class="identity">
      <p class="name">DANA WHITFIELD, PE</p>
      <p class="credentials">HFDP, LEED AP</p>
      <p class="role">CEO/Principal</p>
    </div>
    <div class="divider"></div>
    <ul class="contact">
      <li>(530) 555-0147</li>
      <li>dana.whitfield@k4eng.com</li>
      <li>k4eng.com</li>
      <li>2307 Larkmoor, Alder, CA 92741</li>
    </ul>
  </section>

  <section class="card card-back" aria-label="Business card back">
    <div class="pattern-field" role="img" aria-label="Low-poly faceted triangle pattern in black and grey tones"></div>
    <div class="wordmark">K4</div>
    <p class="tagline">Designing Tomorrow Now</p>
  </section>
</body>
</html>
```